Business Card

Company: Willow Ridge Nursery.

Use uploaded logo or design one just like it. This is a tree growing operation and really like earth tone colors.

Target Market(s)

Landscaping company's, retail nurseries, and landscape arc.

Industry/Entity Type

Business

Font styles to use
Serif

Requirements
Must have
• Name: Dale Whitford
Title: Owner
Address: 48217 W. 150 Road, Grove, OK 74592
Office: 918-555-3172
Cell: 918-555-6094
Fax: 918-555-4418
email: dalewr@plainsmail.net
Willow Ridge Nursery

```html
<!DOCTYPE html>
<html lang="en">
<head>
<meta charset="utf-8">
<title>Willow Ridge Nursery – Business Card</title>
<link rel="stylesheet" href="https://fonts.googleapis.com/css2?family=Tinos:wght@400;700&display=swap">
<style>
  :root {
    --field-green: #3fc43f;
    --field-light: #8fe08a;
    --card-peach: #f8dccb;
    --ink: #1c1c1a;
    --art-pale: #cfe9bf;
    --art-mid: #7fcf78;
    --art-deep: #3aa845;
    --rule-green: #3cb84a;
  }
  html, body {
    margin: 0;
    padding: 0;
    overflow: hidden;
  }
  .canvas {
    position: relative;
    width: 1200px;
    height: 667px;
    overflow: hidden;
    background:
      radial-gradient(ellipse 260px 90px at 180px 20px, var(--field-light), transparent 70%),
      radial-gradient(ellipse 220px 80px at 1000px 650px, var(--field-light), transparent 70%),
      radial-gradient(ellipse 160px 120px at 1180px 120px, var(--field-light), transparent 70%),
      radial-gradient(ellipse 200px 70px at 620px 655px, #6fd66b, transparent 70%),
      var(--field-green);
    font-family: "Tinos", "Times New Roman", serif;
    color: var(--ink);
  }
  .card {
    position: absolute;
    left: 42px;
    top: 42px;
    width: 1117px;
    height: 582px;
    background: var(--card-peach);
  }
  .tree-art {
    position: absolute;
    left: 8px;
    top: 6px;
    width: 360px;
    height: 528px;
    border-radius: 28px;
    background: linear-gradient(180deg, var(--art-pale) 0%, var(--art-mid) 60%, var(--art-deep) 100%);
  }
  .nursery-name {
    position: absolute;
    left: 4px;
    top: 546px;
    margin: 0;
    font-weight: 700;
    font-size: 24px;
    line-height: 1;
    letter-spacing: 0.3px;
    white-space: nowrap;
  }
  .owner {
    position: absolute;
    left: 904px;
    top: 24px;
    margin: 0;
    font-weight: 700;
    font-size: 30px;
    line-height: 40px;
  }
  .owner .title { display: block; padding-left: 4px; }
  .headline {
    position: absolute;
    left: 398px;
    top: 148px;
    margin: 0;
    font-weight: 700;
    font-size: 64px;
    line-height: 1;
    letter-spacing: 0.5px;
    white-space: nowrap;
  }
  .subline {
    position: absolute;
    left: 400px;
    top: 228px;
    margin: 0;
    font-weight: 700;
    font-size: 36px;
    line-height: 1;
    letter-spacing: 0.5px;
    white-space: nowrap;
  }
  .address {
    position: absolute;
    left: 398px;
    top: 360px;
    width: 636px;
    margin: 0;
    padding-bottom: 5px;
    border-bottom: 3px solid var(--rule-green);
    font-size: 39px;
    line-height: 1;
    letter-spacing: 0.6px;
    white-space: nowrap;
  }
  .contacts {
    position: absolute;
    left: 398px;
    top: 414px;
    margin: 0;
    display: grid;
    grid-template-columns: 116px auto;
    font-size: 39px;
    line-height: 42px;
    letter-spacing: 0.6px;
  }
  .contacts dt, .contacts dd { margin: 0; white-space: nowrap; }
</style>
</head>
<body>
<div class="canvas">
  <section class="card">
    <div class="tree-art" role="img" aria-label="Green line illustration of a tree with a leafy crown and a small shrub, planted in a root ball"></div>
    <p class="nursery-name">Willow Ridge Nursery</p>

    <p class="owner">Dale Whitford<span class="title">Owner</span></p>

    <h1 class="headline">Landscaping company's</h1>
    <p class="subline">retail nurseries, and landscape arc</p>

    <p class="address">48217 W. 150 Road, Grove, OK 74592</p>
    <dl class="contacts">
      <dt>Office:</dt><dd>918-555-3172</dd>
      <dt>Fax</dt><dd>: 918-555-4418</dd>
      <dt>Cell</dt><dd>: 918-555-6094</dd>
      <dt>email</dt><dd>: dalewr@plainsmail.net</dd>
    </dl>
  </section>
</div>
</body>
</html>
```